Real Estate Business Cards

Looking for a clean, sharp and professional look for our Real Estate investment Fund that invests in Multi Family Apartment buildings.

Target Market(s)

Real Estate Fund

Industry/Entity Type

Real Estate

Contact Information for Business Card

Company Description: Real Estate Investment Fund
Company Name: RKW Holdings
Name: Marcus Olvane
Cell: (917) 482-0657
Email: marcus@rkwholdings-example.com
Website: www.rkwholdings-example.com
Address: 418, 9th Street, Brooklyn NY 11218

Colors

Designer to choose colors to be used in the design.

Requirements
Nice to have
• Colors to match logo

```html
<!DOCTYPE html>
<html lang="en">
<head>
<meta charset="utf-8">
<title>RKW Holdings – Business Card</title>
<link rel="stylesheet" href="https://fonts.googleapis.com/css2?family=Open+Sans:wght@400;600;700&display=swap">
<style>
  :root {
    --backdrop: #a6a6a6;
    --brand-blue: #0f78b3;
    --card-white: #ffffff;
    --ink: #4a4a4a;
    --rule: #1b74b0;
  }
  * { margin: 0; padding: 0; box-sizing: border-box; }
  html, body { width: 1133px; height: 1200px; overflow: hidden; }
  body {
    background: var(--backdrop);
    font-family: "Open Sans", Arial, sans-serif;
    position: relative;
  }
  .card {
    position: absolute;
    left: 219px;
    width: 694px;
    height: 396px;
  }
  .card-front {
    top: 153px;
    background: var(--brand-blue);
    display: flex;
    align-items: center;
    justify-content: center;
    gap: 16px;
  }
  .brand-square {
    width: 22px;
    height: 22px;
    flex: none;
  }
  .card-front .brand-square { background: var(--card-white); }
  .card-front .brand-name {
    color: var(--card-white);
    font-size: 40px;
    font-weight: 600;
    letter-spacing: 0.5px;
  }
  .card-back {
    top: 649px;
    background: var(--card-white);
  }
  .back-brand {
    position: absolute;
    left: 33px;
    top: 50px;
    display: flex;
    align-items: center;
    gap: 14px;
  }
  .card-back .brand-square { background: var(--brand-blue); width: 20px; height: 20px; }
  .card-back .brand-name {
    color: var(--brand-blue);
    font-size: 30px;
    font-weight: 600;
  }
  .holder-name {
    position: absolute;
    right: 33px;
    top: 229px;
    color: var(--brand-blue);
    font-size: 26px;
    font-weight: 700;
    letter-spacing: 0.3px;
  }
  .divider {
    position: absolute;
    left: 33px;
    right: 33px;
    top: 274px;
    height: 1.5px;
    background: var(--rule);
  }
  .contact-list {
    position: absolute;
    left: 33px;
    top: 291px;
    list-style: none;
    color: var(--ink);
    font-size: 19px;
    line-height: 25.5px;
  }
  .contact-list li { display: flex; align-items: center; gap: 5px; }
  .contact-list svg { width: 16px; height: 16px; fill: var(--brand-blue); flex: none; }
  .address {
    position: absolute;
    right: 33px;
    top: 291px;
    text-align: right;
    color: var(--ink);
    font-size: 19px;
    line-height: 25.5px;
    font-style: normal;
  }
</style>
</head>
<body>
  <section class="card card-front">
    <span class="brand-square"></span>
    <span class="brand-name">RKW Holdings</span>
  </section>

  <section class="card card-back">
    <div class="back-brand">
      <span class="brand-square"></span>
      <span class="brand-name">RKW Holdings</span>
    </div>

    <h1 class="holder-name">MARCUS OLVANE</h1>
    <div class="divider"></div>

    <ul class="contact-list">
      <li>
        <svg viewBox="0 0 16 16" aria-hidden="true"><path d="M3.6 1.5l2.3 2.6-1.3 1.7c.9 2 2.6 3.7 4.6 4.6l1.7-1.3 2.6 2.3-1.4 2.1C7 13.2 2.8 9 1.5 3z"/></svg>
        (917) 482-0657
      </li>
      <li>
        <svg viewBox="0 0 16 16" aria-hidden="true"><path d="M1.5 4h13v1.2L8 9 1.5 5.2z M1.5 6.6L8 10.4l6.5-3.8V12h-13z"/></svg>
        marcus@rkwholdings-example.com
      </li>
      <li>
        <svg viewBox="0 0 16 16" aria-hidden="true"><circle cx="8" cy="8" r="6.5"/></svg>
        www.rkwholdings-example.com
      </li>
    </ul>

    <address class="address">
      418, 9th Street<br>
      Brooklyn NY 11218
    </address>
  </section>
</body>
</html>
```